Cover for Every door Opens Where Every Door Opens

Book Cover Request
Format: Print and electronic (Quillmart)
Book Title: Every Door Opens Where Every Door Opens: Practical Roadmap for Courage and Progress
Author: R.K. Vantreel
Description: This self-help book, written by me, a self-proclaimed nobody, is filled with actionable insights and proven strategies that can help anyone. It combines humor with a serious undertone to deliver practical advice without the typical "self-helpy" vibe.
Catchphrase for the Cover: "Go from Oh Shit to Crushing It!" (or something similar)
Style: I want the cover to reflect my personality—funny, yet serious when needed. I'm open to suggestions and would love to see a design that captures the essence of the book without being too typical of the self-help genre.
Additional Information: I've attached a rough draft of the Quillmart description for more context.
Thank you for your help!
Target Market(s)
Anyone. but id say over 25
Requirements
Nice to have
- Honestly im really at a loss. Im hoping the description will help guide you. I gues i would like it to satand out of course. Be diffrent....but i know how crazy that sounds because everyone wants that. Just give me soem ideas!

```html
<!DOCTYPE html>
<html lang="en">
<head>
<meta charset="utf-8">
<title>Every Door Opens Where Every Door Opens — Cover Wrap</title>
<link rel="stylesheet" href="https://fonts.googleapis.com/css2?family=Bebas+Neue&family=Poppins:wght@300;400;600;700;800&display=swap">
<style>
  :root {
    --page: #ffffff;
    --amber-light: #fdd835;
    --amber: #fbb324;
    --orange: #f7931e;
    --ink: #262626;
    --paper: #ffffff;
    --snow: #f1f1f3;
    --accent: #f9a61c;
  }
  * { margin: 0; padding: 0; box-sizing: border-box; }
  html, body { width: 1200px; height: 1200px; overflow: hidden; background: var(--page); }
  .canvas { position: relative; width: 1200px; height: 1200px; background: var(--page); }

  .cover {
    position: absolute; left: 28px; top: 181px; width: 1129px; height: 808px; overflow: hidden;
    background:
      radial-gradient(ellipse 60% 55% at 78% 8%, var(--amber-light) 0%, var(--amber) 45%, transparent 80%),
      linear-gradient(180deg, var(--amber) 0%, var(--orange) 100%);
    font-family: 'Poppins', sans-serif;
  }
  .tear-band { position: absolute; left: 0; top: 0; width: 1129px; height: 808px; filter: drop-shadow(0 2px 3px rgba(0,0,0,.25)); }
  .bebas { font-family: 'Bebas Neue', 'Oswald', sans-serif; font-weight: 400; }

  /* Back cover */
  .back-title {
    position: absolute; left: 22px; top: 30px; width: 500px;
    display: flex; justify-content: center; align-items: flex-end; gap: 6px;
  }
  .title-stack { display: flex; flex-direction: column; align-items: center; }
  .title-stack .small { color: var(--snow); font-weight: 700; font-size: 27px; line-height: 1; }
  .title-stack .big { color: var(--ink); font-size: 74px; line-height: .9; }
  .back-title .joiner { color: var(--snow); font-weight: 700; font-size: 24px; line-height: 1; margin-bottom: 30px; }

  .subtitle { text-align: center; position: absolute; }
  .subtitle .lead { color: var(--snow); font-weight: 600; line-height: 1; display: block; }
  .subtitle .main { color: var(--ink); font-weight: 700; line-height: 1; display: block; white-space: nowrap; }
  .subtitle .main .and { font-size: .6em; font-weight: 600; color: var(--snow); vertical-align: .35em; }
  .back-subtitle { left: 22px; width: 500px; top: 130px; }
  .back-subtitle .lead { font-size: 17px; margin-bottom: 3px; }
  .back-subtitle .main { font-size: 26px; }

  .blurb {
    position: absolute; left: 22px; top: 199px; width: 503px;
    font-size: 13.6px; line-height: 16px; color: var(--ink); text-align: justify; text-align-last: center;
  }
  .inside-heading {
    position: absolute; left: 26px; top: 367px; color: var(--accent);
    font-weight: 700; font-size: 21px; letter-spacing: .01em;
  }
  .inside-list {
    position: absolute; left: 28px; top: 401px; width: 525px; list-style: none;
    color: var(--snow); font-size: 11.1px; line-height: 13px; font-weight: 300; text-align: justify;
  }
  .inside-list li { margin-bottom: 13px; }
  .inside-list li::before { content: "•"; color: var(--accent); margin-right: 6px; }

  /* Spine */
  .spine-title, .spine-author {
    position: absolute; left: 446px; width: 240px; transform: rotate(90deg);
    display: flex; justify-content: center; align-items: flex-end;
  }
  .spine-title { top: 127px; height: 56px; gap: 4px; }
  .spine-title .title-stack .small { font-size: 13px; }
  .spine-title .title-stack .big { font-size: 38px; }
  .spine-title .joiner { color: var(--snow); font-weight: 700; font-size: 12px; margin-bottom: 12px; }
  .spine-author {
    top: 504px; height: 30px; align-items: center;
    color: var(--snow); font-weight: 600; font-size: 21px; letter-spacing: .55em; white-space: nowrap;
  }

  /* Front cover */
  .front { position: absolute; left: 594px; top: 0; width: 535px; height: 808px; text-align: center; }
  .front > * { position: absolute; left: 0; width: 100%; white-space: nowrap; }
  .front-author { top: 40px; color: var(--snow); font-weight: 600; font-size: 34px; letter-spacing: .5em; padding-left: .5em; line-height: 1; }
  .front-line { font-weight: 800; line-height: 1; }
  .front-line.white { color: var(--snow); }
  .front-line.every-1 { top: 85px; font-size: 72px; }
  .front-line.opens-1 { top: 147px; font-size: 166px; color: var(--ink); }
  .front-line.where { top: 354px; font-size: 94px; }
  .front-line.every-2 { top: 444px; font-size: 72px; }
  .front-line.opens-2 { top: 503px; font-size: 166px; color: var(--accent); }
  .front-subtitle { top: 694px; }
  .front-subtitle .lead { font-size: 29px; margin-bottom: 5px; }
  .front-subtitle .main { font-size: 41px; }
</style>
</head>
<body>
<div class="canvas">
  <div class="cover">
    <svg class="tear-band" viewBox="0 0 1129 808" aria-hidden="true">
      <path fill="#262626" stroke="#ffffff" stroke-width="10" stroke-linejoin="round"
        d="M-20,336 L0,335 L40,325 L80,322 L110,318 L150,313 L190,322 L230,320 L260,330 L290,342 L320,350 L360,345 L400,352 L440,348 L480,350 L520,352 L560,345 L590,338 L620,328 L650,335 L690,340 L720,332 L760,336 L800,345 L850,350 L900,345 L950,348 L1000,352 L1050,350 L1100,355 L1150,352
           L1150,706 L1129,705 L1090,700 L1050,695 L1000,690 L950,688 L900,683 L850,682 L800,680 L760,678 L720,676 L690,685 L660,690 L630,680 L600,670 L570,662 L540,668 L500,668 L450,670 L400,668 L350,670 L300,668 L250,672 L200,670 L150,671 L100,669 L50,671 L0,668 L-20,668 Z"/>
    </svg>

    <!-- Back cover -->
    <div class="back-title">
      <div class="title-stack"><span class="small">EVERY DOOR</span><span class="big bebas">OPENS</span></div>
      <span class="joiner">WHERE</span>
      <div class="title-stack"><span class="small">EVERY DOOR</span><span class="big bebas">OPENS</span></div>
    </div>
    <div class="subtitle back-subtitle">
      <span class="lead">PRACTICAL ROADMAP FOR</span>
      <span class="main">COURAGE <span class="and">AND</span> PROGRESS</span>
    </div>
    <p class="blurb">Are you tired of feeling like a hamster on a wheel, running fast but going nowhere? Dive into "Every Door Opens Where Every Door Opens," your ultimate guide to breaking free from the cycle of sameness and igniting transformative change in your life. This book is not just a collection of self-help clichés; it's a hard-hitting, humorous, and deeply personal roadmap for achieving phenomenal courage and progress.</p>
    <h2 class="inside-heading">WHAT'S INSIDE?</h2>
    <ul class="inside-list">
      <li>Real-Life Stories &amp; Relatable Lessons: Get up close and personal with the author's journey, filled with highs, lows, and everything in between. From battling addiction and navigating divorce to climbing the corporate ladder, these candid stories offer powerful insights and a hefty dose of humor.</li>
      <li>Practical Steps for Transformation: Move from inertia to action with a structured, step-by-step guide that covers all areas of life—personal, professional, and beyond. Whether you're looking to boost your career, improve your relationships, or simply become a better version of yourself, this book has you covered.</li>
      <li>Inspiration &amp; Motivation: Discover why change is not just necessary but exhilarating. Learn to embrace the discomfort of change and turn it into a powerful catalyst for success. The book emphasizes that meaningful change starts with small, consistent steps.</li>
      <li>Tools &amp; Strategies for Success: Equip yourself with practical tools and strategies to manage procrastination, develop patience, and recognize opportunities. Detailed instructions ensure you can apply these concepts in real life, driving you toward your goals.</li>
    </ul>

    <!-- Spine -->
    <div class="spine-title">
      <div class="title-stack"><span class="small">EVERY DOOR</span><span class="big bebas">OPENS</span></div>
      <span class="joiner">WHERE</span>
      <div class="title-stack"><span class="small">EVERY DOOR</span><span class="big bebas">OPENS</span></div>
    </div>
    <div class="spine-author">R.K. VANTREEL</div>

    <!-- Front cover -->
    <div class="front">
      <div class="front-author">R.K. VANTREEL</div>
      <div class="front-line white every-1">EVERY DOOR</div>
      <div class="front-line bebas opens-1">OPENS</div>
      <div class="front-line white where">WHERE</div>
      <div class="front-line white every-2">EVERY DOOR</div>
      <div class="front-line bebas opens-2">OPENS</div>
      <div class="subtitle front-subtitle">
        <span class="lead">PRACTICAL ROADMAP FOR</span>
        <span class="main">COURAGE <span class="and">AND</span> PROGRESS</span>
      </div>
    </div>
  </div>
</div>
</body>
</html>
```